Redesign our business card for more impact

We want to completely replace the back design of our card, and refresh or even change the front entirely. We are happy with our black Q7 logo and do not want to change it.
Our company address changed too. It is now 58 Corvallen, Irvine, CA 92741
Updates

It was reported by Sketch Harbor email today that the uploaded files didnt upload. I am trying again.

Target Market(s)

Architects and Building Owners (People making multi-million dollar decisions)

Industry/Entity Type

Consulting Engineering

Contact Information for Business Card

Contact info on the front. "wallpaper" design on back with tag line on the back "Engineering Your Future"

Font styles to use
Sans Serif

Requirements
Must have
• A vivid, modern, impactful ...but tasteful back of card design. It should communicate our premier status, but grab attention as innovative. DESIGN SHOULD BE ELEGANT AND NOT TOO BUSY.
Nice to have
• Repeating pattern, multi-color, something creative...
Should not have
• Anything that looks too playful or that we are not serious professionals. It should also not be too boring or conservative.

```html
<!DOCTYPE html>
<html lang="en">
<head>
<meta charset="utf-8">
<title>Q7 Business Card</title>
<link rel="stylesheet" href="https://fonts.googleapis.com/css2?family=Arimo:wght@400;700&family=Montserrat:wght@500;700;800&display=swap">
<style>
  :root {
    --page: #eef0ef;
    --ink: #161616;
    --black: #0b0b0b;
    --pattern-dark: #1b1b1b;
    --pattern-light: #262626;
    --red: #9a0000;
    --white: #ffffff;
    --grey: #3a3a3a;
  }
  * { margin: 0; padding: 0; box-sizing: border-box; }
  html, body { width: 1200px; height: 1200px; overflow: hidden; }
  body {
    background: var(--page);
    display: flex;
    flex-direction: column;
    align-items: center;
    justify-content: center;
    gap: 44px;
  }
  .card {
    width: 900px;
    height: 514px;
    position: relative;
    overflow: hidden;
    box-shadow: 0 10px 30px rgba(0,0,0,0.12);
  }

  /* Back side */
  .card-back { background: var(--black); }
  .back-pattern {
    position: absolute; inset: 0;
    background: linear-gradient(135deg, var(--pattern-dark) 0%, var(--black) 45%, var(--pattern-light) 100%);
  }
  .back-content {
    position: absolute; left: 0; right: 0; top: 120px;
    text-align: center;
    color: var(--white);
    font-family: "Montserrat", sans-serif;
  }
  .back-logo {
    font-weight: 800;
    font-size: 82px;
    line-height: 1;
  }
  .back-descriptor {
    margin-top: 26px;
    font-weight: 500;
    font-size: 22px;
    letter-spacing: 0.32em;
  }
  .tagline-band {
    position: absolute; left: 0; right: 0; bottom: 0;
    height: 118px;
    background: var(--red);
    border-top: 4px solid var(--black);
    display: flex; align-items: center; justify-content: center;
  }
  .tagline {
    color: var(--white);
    font-family: "Montserrat", sans-serif;
    font-weight: 800;
    font-size: 34px;
    letter-spacing: 0.22em;
  }

  /* Front side */
  .card-front {
    background: var(--white);
    display: flex;
    align-items: center;
  }
  .front-logo {
    width: 400px;
    text-align: center;
    font-family: "Arimo", sans-serif;
    font-weight: 700;
    font-size: 190px;
    color: var(--ink);
    line-height: 1;
  }
  .divider {
    width: 4px;
    height: 300px;
    background: var(--ink);
  }
  .contact {
    padding-left: 44px;
    font-family: "Arimo", sans-serif;
    color: var(--grey);
  }
  .contact-name {
    color: var(--red);
    font-weight: 700;
    font-size: 38px;
    line-height: 1.05;
  }
  .contact-role {
    margin-top: 6px;
    font-size: 17px;
    line-height: 1.2;
  }
  .contact-list {
    list-style: none;
    margin-top: 22px;
    font-size: 21px;
  }
  .contact-list li {
    display: flex; align-items: center; gap: 14px;
    margin-bottom: 12px;
  }
  .contact-list svg { width: 24px; height: 24px; flex: none; }
</style>
</head>
<body>

<section class="card card-back">
  <div class="back-pattern" role="img" aria-label="Dark repeating wallpaper pattern of the company mark"></div>
  <div class="back-content">
    <div class="back-logo">Q7</div>
    <div class="back-descriptor">HEALTHCARE ENGINEERING EXPERTS</div>
  </div>
  <div class="tagline-band">
    <p class="tagline">"ENGINEERING YOUR FUTURE"</p>
  </div>
</section>

<section class="card card-front">
  <div class="front-logo">Q7</div>
  <div class="divider"></div>
  <div class="contact">
    <h1 class="contact-name">DANIEL WHITFIELD, PE</h1>
    <p class="contact-role">HFDP, LEED AP<br>CEO/Principal</p>
    <ul class="contact-list">
      <li>
        <svg viewBox="0 0 24 24"><circle cx="12" cy="12" r="10" fill="#9a0000"/><circle cx="12" cy="12" r="4" fill="#fff"/></svg>
        58 Corvallen, Irvine, CA 92741
      </li>
      <li>
        <svg viewBox="0 0 24 24"><path fill="#9a0000" d="M6.6 10.8a15 15 0 0 0 6.6 6.6l2.2-2.2a1 1 0 0 1 1-.25 11.4 11.4 0 0 0 3.6.57 1 1 0 0 1 1 1V20a1 1 0 0 1-1 1A17 17 0 0 1 3 4a1 1 0 0 1 1-1h3.5a1 1 0 0 1 1 1c0 1.25.2 2.45.57 3.57a1 1 0 0 1-.25 1z"/></svg>
        (626) 555-0147
      </li>
      <li>
        <svg viewBox="0 0 24 24"><rect x="2" y="5" width="20" height="14" fill="#9a0000"/><path d="M2 5l10 8 10-8" fill="none" stroke="#fff" stroke-width="1.6"/></svg>
        daniel.whitfield@q7eng.com
      </li>
      <li>
        <svg viewBox="0 0 24 24"><circle cx="12" cy="12" r="10" fill="#9a0000"/><g fill="none" stroke="#fff" stroke-width="1.3"><ellipse cx="12" cy="12" rx="4.5" ry="10"/><path d="M2 12h20M4 7h16M4 17h16"/></g></svg>
        www.q7eng.com
      </li>
    </ul>
  </div>
</section>

</body>
</html>
```